Need some visual "dash" to a dashboard UI design

Have a project that needs a little visual "zip". Attached are some screenshots of the current design. Will need source files of design work, Photoshop preferred, but Illustrator or other source will be acceptable. Please confirm before starting the work.

Here is a working prototype:
https://pm47rq.velnoria.com/#g=1&p=scenario_1_-_dashboard_view

Work has been done to get the UI elements in place, but need a little visual improvement to make it really "pop" ...while retaining its usability.

Primarily need some visual design done for the left column 5 elements revealing values for tech in and tech out between 0 and 20. Auth OT values are 0min, 30min, 60min, 90min, 120min, and "over 2 hours". Avail Reserve Capacity will be 0% through 10%. And Supply Delta can range from -10,000 to +10,000

Some design for the charts on the right would be great. Just trying to establish a visual language to apply to these values.

Please use colors from the approved palette with hex values (plus black and white):

Primary
Orange ff7200
Orange Highlight fcb314
Blue 067ab4
Blue Highlight 3aa5dc

Secondary
Lime b6bf00
Lime Highlight dbd810
Green 6ebb1f
Green Highlight c4d82d
Burgundy b30a3c
Burgundy Highlight da3872
Purple 81017e
Purple Highlight b8509e
Dark Blue 0c2577
Dark Blue Highlight 020bb3

Accent
Ochre eaab00
Magenta ff0066
Royal Blue 000066
Yellow ffef00
Teal 00c7b2
Dusty Blue 96b1d0
Light Blue bcc9d6
Mint Green 99ffcc
Gold ff9900
Taupe cccc66
Warm Gray cccc99

Industry/Entity Type

Work

Number of Pages Required

2 page

Font styles to use
Sans Serif

Requirements
Must have
• Must conform to the overall page layout described in the design doc attached. Must conform to the corporate color palette attached in the description.
• sorry, forgot to mention font: must use Verdana
• Verdana Font Family
• Verdana Regular
• Verdana Italic
• Verdana Bold
• Verdana Bold Italic

```html
<!DOCTYPE html>
<html lang="en">
<head>
<meta charset="utf-8">
<title>VANTIX Capacity Planning – Dashboard</title>
<link href="https://fonts.googleapis.com/css2?family=Roboto+Condensed:wght@400;500;700&family=Roboto:wght@400;500;700&display=swap" rel="stylesheet">
<style>
:root{
  --nav-top:#1654aa;
  --nav-sub:#0e4391;
  --nav-active:#2569c2;
  --gold:#f5b800;
  --blue:#1464a8;
  --blue-bright:#2e8fd8;
  --blue-light:#3a9ad8;
  --blue-dark:#0d56a3;
  --orange:#f7a21b;
  --green:#5cb82a;
  --red:#e2231a;
  --panel:#e9e9eb;
  --panel-left:#f2f2f2;
  --line:#cfcfcf;
  --ink:#222;
  --ink-soft:#555;
  --white:#fff;
}
*{box-sizing:border-box;margin:0;padding:0}
html,body{width:1200px;height:888px;overflow:hidden;background:var(--white)}
body{position:relative;font-family:"Roboto",sans-serif;color:var(--ink)}
.abs{position:absolute}
.cond{font-family:"Roboto Condensed",sans-serif}

/* top navigation */
.topbar{left:0;top:0;width:1200px;height:51px;background:var(--nav-top)}
.brand{left:13px;top:9px;display:flex;align-items:center;gap:8px;color:var(--white);font:700 19px "Roboto Condensed",sans-serif;letter-spacing:.5px}
.brand-dot{width:26px;height:26px;border:2px solid var(--white);border-radius:50%}
.nav-tab{top:0;height:51px;color:var(--white);font:500 9.5px "Roboto",sans-serif;text-align:center}
.nav-tab svg{display:block;margin:9px auto 4px}
.nav-tab.active{background:var(--nav-active);border-top:3px solid var(--gold)}
.subnav{left:0;top:51px;width:1200px;height:19px;background:var(--nav-sub)}
.subnav a{position:absolute;top:3px;color:var(--white);font:500 9px "Roboto",sans-serif;text-decoration:none;text-align:center}
.subnav a.current{border:1px solid var(--white);top:3px;height:14px;padding-top:1px}

/* left action column */
.action-panel{left:24px;top:99px;width:375px;height:716px;background:var(--panel-left);border:1px solid var(--line)}
.action-for{left:14px;top:17px;font:700 11.5px "Roboto Condensed",sans-serif}
.select{background:var(--white);border:1px solid #bbb;font:400 11px "Roboto",sans-serif;padding:0 9px;display:flex;align-items:center;justify-content:space-between}
.tabs{left:0;top:49px;width:374px;height:35px;display:flex;font:500 11.5px "Roboto Condensed",sans-serif;color:var(--white)}
.tabs div{display:flex;align-items:center;justify-content:center}
.tab-action{width:186px;background:var(--orange)}
.tab-review{flex:1;background:var(--blue)}
.days{left:10px;top:103px;width:352px;height:42px;display:flex;background:var(--white);border:1px solid #bbb}
.day{padding:9px 0 0 0;font:400 9.5px "Roboto",sans-serif;border-right:1px solid #ccc}
.day b{display:block;color:var(--blue);font-weight:700;margin-top:2px}
.day.sel{background:var(--orange);color:var(--white)}
.day.sel b{color:var(--white)}

.site{left:0;width:373px;border-top:1px solid var(--line)}
.site.closed{background:var(--blue-bright);color:var(--white)}
.site-name{left:14px;top:22px;font:500 11.5px "Roboto Condensed",sans-serif}
.badge{right:16px;top:23px;height:16px;padding:0 6px;font:500 10px "Roboto Condensed",sans-serif;color:var(--white);display:flex;align-items:center;background:var(--green)}
.badge.off{background:var(--orange)}
.widget-label{font:400 8.5px "Roboto",sans-serif;color:var(--ink-soft)}
.site.closed .widget-label.free{color:var(--white)}
.box{background:var(--white);border:1px solid #bbb;height:45px;top:48px}
.inout{left:14px;width:44px}
.out{left:68px;top:48px;width:40px;height:45px}
.auth{left:115px;width:79px}
.avail{left:206px;top:48px;width:64px;height:45px}
.delta{left:284px;width:77px}
.meter{height:5px;background:#e4e4e4;border:1px solid #ccc}
.meter i{display:block;height:100%}
.pct{font:400 7.5px "Roboto",sans-serif;color:var(--ink-soft)}
.site.closed .pct{color:var(--white)}
.delta-val{left:25px;top:23px;font:700 11px "Roboto Condensed",sans-serif;color:var(--blue)}
.plus{font:700 10px "Roboto Condensed",sans-serif;color:var(--blue)}
.btn{top:111px;height:39px;background:var(--blue-dark);color:var(--white);font:500 12.5px "Roboto Condensed",sans-serif;display:flex;align-items:center;justify-content:center;letter-spacing:.2px}

/* right area */
.filter-bar{left:419px;top:98px;width:761px;height:84px;background:var(--blue-bright);color:var(--white)}
.filter-label{font:500 12px "Roboto Condensed",sans-serif}
.date-field{background:var(--white);font:400 11px "Roboto",sans-serif;color:var(--ink);padding:0 9px;display:flex;align-items:center;justify-content:space-between}
.date-field.disabled{background:#5aaee6;color:#cfe8fa}
.check{width:12px;height:12px;background:var(--white)}
.card{background:var(--panel)}
svg text{font-family:"Roboto",sans-serif}
.svg-title{font-family:"Roboto Condensed",sans-serif;font-weight:700}

.footer{left:0;top:839px;width:1200px;height:49px;background:var(--nav-top);color:var(--white);font:400 11.5px "Roboto",sans-serif}
</style>
</head>
<body>

<!-- navigation -->
<header>
  <div class="abs topbar"></div>
  <div class="abs brand"><span class="brand-dot"></span>VANTIX</div>
  <div class="abs nav-tab active" style="left:125px;width:104px">
    <svg width="34" height="20" viewBox="0 0 34 20" fill="none" stroke="#f5b800" stroke-width="1.6"><rect x="6" y="3" width="7" height="6"/><rect x="19" y="1" width="9" height="6"/><path d="M3 16 L31 8"/><path d="M17 12 L14 18 L20 18 Z" fill="#f5b800"/></svg>
    Capacity Planning
  </div>
  <div class="abs nav-tab" style="left:229px;width:60px">
    <svg width="20" height="20" viewBox="0 0 20 20"><circle cx="10" cy="10" r="8.5" fill="none" stroke="#fff" stroke-width="1.5"/><circle cx="6" cy="10" r="1.4" fill="#fff"/><circle cx="10" cy="10" r="1.4" fill="#fff"/><circle cx="14" cy="10" r="1.4" fill="#fff"/></svg>
    More
  </div>
  <nav class="abs subnav">
    <a class="current" style="left:23px;width:86px">Dashboard</a>
    <a style="left:150px;width:40px">Lights</a>
    <a style="left:250px;width:50px">Daily Plan</a>
    <a style="left:345px;width:72px">Long Term Plan</a>
    <a style="left:465px;width:115px">Schedule Recommendation</a>
    <a style="left:642px;width:40px">Config</a>
  </nav>
</header>

<!-- action column -->
<section class="abs action-panel">
  <div class="abs action-for">ACTION FOR</div>
  <div class="abs select" style="left:86px;top:10px;width:275px;height:29px">East Mountain Shores <svg width="8" height="12" viewBox="0 0 8 12"><path d="M4 0 L8 4 H0Z M4 12 L8 8 H0Z" fill="#222"/></svg></div>
  <div class="abs tabs"><div class="tab-action">ACTION REQUIRES (4)</div><div class="tab-review">REVIEW REQUIRES (9)</div></div>
  <div class="abs days">
    <div class="day" style="width:80px;padding-left:24px">TODAY<b>03.12</b></div>
    <div class="day" style="width:122px;padding-left:28px">TOMORROW<b>03.13</b></div>
    <div class="day sel" style="width:60px;padding-left:18px">+2<b>03.14</b></div>
    <div class="day" style="flex:1;padding-left:38px;border-right:0">+3<b>03.15</b></div>
  </div>

  <!-- site: Hopkinsville -->
  <div class="abs site" style="top:177px;height:122px">
    <div class="abs site-name">HOPKINSVILLE_CB</div>
    <div class="abs badge">OPEN</div>
    <div class="abs box inout">
      <span class="abs widget-label" style="left:7px;top:7px">IN</span>
      <svg class="abs" style="left:25px;top:8px" width="11" height="8" viewBox="0 0 11 8"><path d="M0 4 L5 0 V2.5 H11 V5.5 H5 V8Z" fill="#1464a8"/></svg>
      <svg class="abs" style="left:6px;top:24px" width="16" height="17" viewBox="0 0 16 17"><circle cx="8" cy="4.5" r="4" fill="#1464a8"/><path d="M1 17 C1 10 15 10 15 17Z" fill="#1464a8"/></svg>
      <span class="abs plus" style="left:24px;top:28px">+5</span>
    </div>
    <div class="abs out">
      <span class="abs widget-label" style="left:2px;top:7px">OUT</span>
      <svg class="abs" style="left:24px;top:8px" width="11" height="8" viewBox="0 0 11 8"><path d="M11 4 L6 0 V2.5 H0 V5.5 H6 V8Z" fill="#1464a8"/></svg>
      <svg class="abs" style="left:4px;top:24px" width="16" height="17" viewBox="0 0 16 17"><circle cx="8" cy="4.5" r="4" fill="#1464a8"/><path d="M1 17 C1 10 15 10 15 17Z" fill="#1464a8"/></svg>
    </div>
    <div class="abs box auth">
      <span class="abs widget-label" style="left:7px;top:7px">AUTH OT</span>
      <svg class="abs" style="left:8px;top:23px" width="12" height="12" viewBox="0 0 12 12"><circle cx="6" cy="6" r="5" fill="none" stroke="#1464a8" stroke-width="1.6"/><path d="M6 3 V6 H8.5" fill="none" stroke="#1464a8" stroke-width="1.3"/></svg>
      <div class="abs meter" style="left:27px;top:27px;width:43px"><i style="width:0"></i></div>
    </div>
    <div class="abs avail">
      <span class="abs widget-label free" style="left:0;top:7px">AVAIL RSV CAB</span>
      <svg class="abs" style="left:0;top:23px" width="17" height="14" viewBox="0 0 17 14"><circle cx="11" cy="3.5" r="3" fill="#7fa9d6"/><circle cx="6" cy="4.5" r="3.4" fill="#1464a8"/><path d="M0 14 C0 7.5 12 7.5 12 14Z" fill="#1464a8"/></svg>
      <div class="abs meter" style="left:19px;top:27px;width:43px"><i style="width:0"></i></div>
      <span class="abs pct" style="right:2px;top:37px">0%</span>
    </div>
    <div class="abs box delta">
      <span class="abs widget-label" style="left:7px;top:7px">SUPPLY DELTA</span>
      <svg class="abs" style="left:7px;top:23px" width="15" height="13" viewBox="0 0 15 13"><path d="M7.5 0 L15 13 H0Z" fill="#f7a21b"/></svg>
      <span class="abs delta-val">+100</span>
    </div>
  </div>

  <!-- site: Bowling Green -->
  <div class="abs site" style="top:299px;height:123px">
    <div class="abs site-name">BOWLING_GREEN_CB</div>
    <div class="abs badge">OPEN</div>
    <div class="abs box inout">
      <span class="abs widget-label" style="left:7px;top:7px">IN</span>
      <svg class="abs" style="left:25px;top:8px" width="11" height="8" viewBox="0 0 11 8"><path d="M0 4 L5 0 V2.5 H11 V5.5 H5 V8Z" fill="#1464a8"/></svg>
      <svg class="abs" style="left:6px;top:24px" width="16" height="17" viewBox="0 0 16 17"><circle cx="8" cy="4.5" r="4" fill="#1464a8"/><path d="M1 17 C1 10 15 10 15 17Z" fill="#1464a8"/></svg>
      <span class="abs plus" style="left:24px;top:28px">+5</span>
    </div>
    <div class="abs out">
      <span class="abs widget-label" style="left:2px;top:7px">OUT</span>
      <svg class="abs" style="left:24px;top:8px" width="11" height="8" viewBox="0 0 11 8"><path d="M11 4 L6 0 V2.5 H0 V5.5 H6 V8Z" fill="#1464a8"/></svg>
      <svg class="abs" style="left:4px;top:24px" width="16" height="17" viewBox="0 0 16 17"><circle cx="8" cy="4.5" r="4" fill="#1464a8"/><path d="M1 17 C1 10 15 10 15 17Z" fill="#1464a8"/></svg>
    </div>
    <div class="abs box auth">
      <span class="abs widget-label" style="left:7px;top:7px">AUTH OT</span>
      <svg class="abs" style="left:8px;top:23px" width="12" height="12" viewBox="0 0 12 12"><circle cx="6" cy="6" r="5" fill="none" stroke="#1464a8" stroke-width="1.6"/><path d="M6 3 V6 H8.5" fill="none" stroke="#1464a8" stroke-width="1.3"/></svg>
      <div class="abs meter" style="left:27px;top:27px;width:43px"><i style="width:0"></i></div>
    </div>
    <div class="abs avail">
      <span class="abs widget-label free" style="left:0;top:7px">AVAIL RSV CAB</span>
      <svg class="abs" style="left:0;top:23px" width="17" height="14" viewBox="0 0 17 14"><circle cx="11" cy="3.5" r="3" fill="#7fa9d6"/><circle cx="6" cy="4.5" r="3.4" fill="#1464a8"/><path d="M0 14 C0 7.5 12 7.5 12 14Z" fill="#1464a8"/></svg>
      <div class="abs meter" style="left:19px;top:27px;width:43px"><i style="width:65%;background:var(--green)"></i></div>
      <span class="abs pct" style="right:2px;top:37px">10%</span>
    </div>
    <div class="abs box delta">
      <span class="abs widget-label" style="left:7px;top:7px">SUPPLY DELTA</span>
      <svg class="abs" style="left:7px;top:23px" width="15" height="13" viewBox="0 0 15 13"><path d="M7.5 0 L15 13 H0Z" fill="#f7a21b"/></svg>
      <span class="abs delta-val">0</span>
    </div>
  </div>

  <!-- site: Memphis North (closed) -->
  <div class="abs site closed" style="top:422px;height:170px;border-top:0">
    <div class="abs site-name" style="top:18px">MEMPHS_NORTH</div>
    <div class="abs badge off" style="top:19px">CLOSED</div>
    <div class="abs box inout" style="top:43px">
      <span class="abs widget-label" style="left:7px;top:7px">IN</span>
      <svg class="abs" style="left:25px;top:8px" width="11" height="8" viewBox="0 0 11 8"><path d="M0 4 L5 0 V2.5 H11 V5.5 H5 V8Z" fill="#1464a8"/></svg>
      <svg class="abs" style="left:6px;top:24px" width="16" height="17" viewBox="0 0 16 17"><circle cx="8" cy="4.5" r="4" fill="#1464a8"/><path d="M1 17 C1 10 15 10 15 17Z" fill="#1464a8"/></svg>
    </div>
    <div class="abs out" style="top:43px">
      <span class="abs widget-label free" style="left:2px;top:7px">OUT</span>
      <svg class="abs" style="left:24px;top:8px" width="11" height="8" viewBox="0 0 11 8"><path d="M11 4 L6 0 V2.5 H0 V5.5 H6 V8Z" fill="#fff"/></svg>
      <svg class="abs" style="left:4px;top:24px" width="16" height="17" viewBox="0 0 16 17"><circle cx="8" cy="4.5" r="4" fill="#fff"/><path d="M1 17 C1 10 15 10 15 17Z" fill="#fff"/></svg>
    </div>
    <div class="abs box auth" style="top:43px">
      <span class="abs widget-label" style="left:7px;top:7px">AUTH OT</span>
      <svg class="abs" style="left:8px;top:23px" width="12" height="12" viewBox="0 0 12 12"><circle cx="6" cy="6" r="5" fill="none" stroke="#1464a8" stroke-width="1.6"/><path d="M6 3 V6 H8.5" fill="none" stroke="#1464a8" stroke-width="1.3"/></svg>
      <div class="abs meter" style="left:27px;top:25px;width:43px"><i style="width:70%;background:var(--orange)"></i></div>
      <span class="abs pct" style="left:41px;top:32px;color:var(--ink)">30 mins</span>
    </div>
    <div class="abs avail" style="top:43px">
      <span class="abs widget-label free" style="left:0;top:7px">AVAIL RSV CAB</span>
      <svg class="abs" style="left:0;top:23px" width="17" height="14" viewBox="0 0 17 14"><circle cx="11" cy="3.5" r="3" fill="#cfe4f6"/><circle cx="6" cy="4.5" r="3.4" fill="#fff"/><path d="M0 14 C0 7.5 12 7.5 12 14Z" fill="#fff"/></svg>
      <div class="abs meter" style="left:19px;top:27px;width:43px"><i style="width:35%;background:var(--green)"></i></div>
      <span class="abs pct" style="right:2px;top:37px">5%</span>
    </div>
    <div class="abs box delta" style="top:43px">
      <span class="abs widget-label" style="left:7px;top:7px">SUPPLY DELTA</span>
      <svg class="abs" style="left:7px;top:23px" width="15" height="13" viewBox="0 0 15 13"><path d="M7.5 0 L15 13 H0Z" fill="#f7a21b"/></svg>
      <span class="abs delta-val">-50</span>
    </div>
    <div class="abs btn" style="left:17px;width:145px">ROLL BACK</div>
    <div class="abs btn" style="left:175px;width:186px">UTILIZE RESERVE CAPACITY</div>
  </div>

  <!-- site: Memphis Jackson -->
  <div class="abs site" style="top:592px;height:123px;border-top:0">
    <div class="abs site-name" style="top:14px">MEMPT_JACKSON_CB</div>
    <div class="abs badge" style="top:15px">OPEN</div>
    <div class="abs box inout" style="top:40px">
      <span class="abs widget-label" style="left:7px;top:7px">IN</span>
      <svg class="abs" style="left:25px;top:8px" width="11" height="8" viewBox="0 0 11 8"><path d="M0 4 L5 0 V2.5 H11 V5.5 H5 V8Z" fill="#1464a8"/></svg>
      <svg class="abs" style="left:6px;top:24px" width="16" height="17" viewBox="0 0 16 17"><circle cx="8" cy="4.5" r="4" fill="#1464a8"/><path d="M1 17 C1 10 15 10 15 17Z" fill="#1464a8"/></svg>
    </div>
    <div class="abs out" style="top:40px">
      <span class="abs widget-label" style="left:2px;top:7px">OUT</span>
      <svg class="abs" style="left:24px;top:8px" width="11" height="8" viewBox="0 0 11 8"><path d="M11 4 L6 0 V2.5 H0 V5.5 H6 V8Z" fill="#1464a8"/></svg>
      <svg class="abs" style="left:4px;top:24px" width="16" height="17" viewBox="0 0 16 17"><circle cx="8" cy="4.5" r="4" fill="#1464a8"/><path d="M1 17 C1 10 15 10 15 17Z" fill="#1464a8"/></svg>
    </div>
    <div class="abs box auth" style="top:40px">
      <span class="abs widget-label" style="left:7px;top:7px">AUTH OT</span>
      <svg class="abs" style="left:8px;top:23px" width="12" height="12" viewBox="0 0 12 12"><circle cx="6" cy="6" r="5" fill="none" stroke="#1464a8" stroke-width="1.6"/><path d="M6 3 V6 H8.5" fill="none" stroke="#1464a8" stroke-width="1.3"/></svg>
      <div class="abs meter" style="left:27px;top:27px;width:43px"><i style="width:0"></i></div>
    </div>
    <div class="abs avail" style="top:40px">
      <span class="abs widget-label free" style="left:0;top:7px">AVAIL RSV CAB</span>
      <svg class="abs" style="left:0;top:23px" width="17" height="14" viewBox="0 0 17 14"><circle cx="11" cy="3.5" r="3" fill="#7fa9d6"/><circle cx="6" cy="4.5" r="3.4" fill="#1464a8"/><path d="M0 14 C0 7.5 12 7.5 12 14Z" fill="#1464a8"/></svg>
      <div class="abs meter" style="left:19px;top:27px;width:43px"><i style="width:65%;background:var(--green)"></i></div>
      <span class="abs pct" style="right:2px;top:37px">10%</span>
    </div>
    <div class="abs box delta" style="top:40px">
      <span class="abs widget-label" style="left:7px;top:7px">SUPPLY DELTA</span>
      <svg class="abs" style="left:7px;top:23px" width="15" height="13" viewBox="0 0 15 13"><path d="M7.5 0 L15 13 H0Z" fill="#f7a21b"/></svg>
      <span class="abs delta-val">+10,990</span>
    </div>
  </div>
</section>

<!-- filter bar -->
<section class="abs filter-bar">
  <div class="abs filter-label" style="left:23px;top:18px">PREVIOUSLY VIEWED</div>
  <div class="abs date-field" style="left:23px;top:40px;width:260px;height:24px">MEMPHIS_NORTH_CB <svg width="8" height="12" viewBox="0 0 8 12"><path d="M4 0 L8 4 H0Z M4 12 L8 8 H0Z" fill="#222"/></svg></div>
  <div class="abs filter-label" style="left:332px;top:18px">TODAY</div>
  <div class="abs date-field" style="left:333px;top:40px;width:108px;height:24px">03.12.2018 <svg width="10" height="10" viewBox="0 0 10 10"><rect x=".5" y="1.5" width="9" height="8" fill="none" stroke="#444"/><path d="M.5 4 H9.5 M3 5.5 V8 M5 5.5 V8 M7 5.5 V8" stroke="#444"/></svg></div>
  <div class="abs check" style="left:487px;top:23px"></div>
  <div class="abs filter-label" style="left:506px;top:22px;font-size:10px">SHOW DATE RANGE</div>
  <div class="abs date-field disabled" style="left:487px;top:40px;width:117px;height:24px">03.12.2018 <svg width="10" height="10" viewBox="0 0 10 10"><rect x=".5" y="1.5" width="9" height="8" fill="none" stroke="#cfe8fa"/><path d="M.5 4 H9.5 M3 5.5 V8 M5 5.5 V8 M7 5.5 V8" stroke="#cfe8fa"/></svg></div>
  <svg class="abs" style="left:649px;top:29px" width="32" height="25" viewBox="0 0 32 25"><path d="M1 0 V24 H32" fill="none" stroke="#fff" stroke-width="1.6"/><rect x="6" y="14" width="4" height="8" fill="#fff"/><rect x="12" y="9" width="4" height="13" fill="#fff"/><rect x="18" y="12" width="4" height="10" fill="#fff"/><rect x="24" y="4" width="4" height="18" fill="#fff"/></svg>
  <svg class="abs" style="left:703px;top:29px" width="28" height="26" viewBox="0 0 28 26"><path d="M0 3 L8 0 V23 L0 26Z M10 0 L18 3 V26 L10 23Z M20 3 L28 0 V23 L20 26Z" fill="#fff"/></svg>
</section>

<!-- supply vs demand chart -->
<section class="abs card" style="left:419px;top:196px;width:761px;height:340px">
  <svg width="761" height="340" viewBox="524 245 951 425">
    <text class="svg-title" x="995" y="304" text-anchor="middle" font-size="19" fill="#333">SUPPLY VS DEMAND (MINUTES)</text>
    <g font-size="14" fill="#333" text-anchor="end">
      <text x="610" y="289">3000</text><text x="610" y="327">2000</text><text x="610" y="365">1000</text><text x="610" y="403">0</text>
      <text x="610" y="441">1000</text><text x="610" y="479">2000</text><text x="610" y="517">3000</text><text x="610" y="555">4000</text>
      <text x="610" y="593">5000</text><text x="610" y="631">6000</text>
    </g>
    <text transform="translate(565 323) rotate(-90)" font-size="13" fill="#333" text-anchor="middle">SUPPLY</text>
    <text transform="translate(565 526) rotate(-90)" font-size="13" fill="#333" text-anchor="middle">DEMAND</text>
    <line x1="625" y1="398.5" x2="1470" y2="398.5" stroke="#999" stroke-width="1"/>
    <g fill="#1464a8">
      <rect x="649" y="372" width="26" height="26"/><rect x="722" y="366" width="26" height="32"/>
      <rect x="910" y="372" width="26" height="26"/><rect x="1000" y="372" width="26" height="26"/>
      <rect x="1100" y="372" width="26" height="26"/><rect x="1198" y="383" width="26" height="15"/>
    </g>
    <g fill="#3a9ad8">
      <rect x="820" y="400" width="26" height="53"/><rect x="1296" y="400" width="26" height="53"/><rect x="1379" y="400" width="26" height="16"/>
    </g>
    <g font-size="12" fill="#222" text-anchor="middle">
      <text x="661" y="363">565</text><text x="735" y="359">750</text><text x="922" y="366">663</text><text x="1012" y="366">663</text>
      <text x="1112" y="365">963</text><text x="1210" y="376">462</text>
      <text x="833" y="473">1250</text><text x="1308" y="472">762</text><text x="1393" y="434">50</text>
      <text x="661" y="420">5:00 <tspan font-size="8" dy="-5">pm</tspan></text>
      <text x="737" y="420">8:00 <tspan font-size="8" dy="-5">pm</tspan></text>
      <text x="832" y="382">11:00 <tspan font-size="8" dy="-5">pm</tspan></text>
      <text x="919" y="420">2:00 <tspan font-size="8" dy="-5">Am</tspan></text>
      <text x="1013" y="420">5:00 <tspan font-size="8" dy="-5">Am</tspan></text>
      <text x="1113" y="420">6:00 <tspan font-size="8" dy="-5">Am</tspan></text>
      <text x="1209" y="420">7:00 <tspan font-size="8" dy="-5">Am</tspan></text>
      <text x="1310" y="385">8:00 <tspan font-size="8" dy="-5">Am</tspan></text>
      <text x="1395" y="385">9:00 <tspan font-size="8" dy="-5">Am</tspan></text>
    </g>
  </svg>
</section>

<!-- work hours -->
<section class="abs card" style="left:419px;top:546px;width:177px;height:270px">
  <svg width="177" height="270" viewBox="524 682 221 337">
    <text class="svg-title" x="542" y="712" font-size="14" fill="#222">WORK HOURS</text>
    <text x="658" y="712" font-size="13" fill="#444">03.12.2018</text>
    <g stroke="#cfcfcf" stroke-width="1">
      <line x1="570" y1="745" x2="727" y2="745"/><line x1="570" y1="777" x2="727" y2="777"/><line x1="570" y1="809" x2="727" y2="809"/>
      <line x1="570" y1="841" x2="727" y2="841"/><line x1="570" y1="873" x2="727" y2="873"/><line x1="570" y1="905" x2="727" y2="905"/>
      <line x1="570" y1="937" x2="727" y2="937"/><line x1="570" y1="965" x2="727" y2="965"/>
    </g>
    <g font-size="13" fill="#333" text-anchor="end">
      <text x="561" y="750">14</text><text x="561" y="782">12</text><text x="561" y="814">10</text><text x="561" y="846">8</text>
      <text x="561" y="878">6</text><text x="561" y="910">4</text><text x="561" y="942">2</text><text x="561" y="974">0</text>
    </g>
    <rect x="589" y="838" width="36" height="127" fill="#1464a8"/><rect x="589" y="828" width="36" height="10" fill="#e8401c"/>
    <rect x="589" y="816" width="36" height="12" fill="#3a9ad8"/><rect x="589" y="805" width="36" height="11" fill="#f7a21b"/>
    <rect x="668" y="812" width="36" height="153" fill="#1464a8"/><rect x="668" y="801" width="36" height="11" fill="#e8401c"/>
    <rect x="668" y="789" width="36" height="12" fill="#3a9ad8"/><rect x="668" y="778" width="36" height="11" fill="#f7a21b"/>
    <text x="607" y="983" font-size="12" fill="#444" text-anchor="middle">Before</text>
    <text x="686" y="986" font-size="12" fill="#444" text-anchor="middle">After</text>
    <g font-size="8" fill="#333">
      <rect x="532" y="1002" width="6" height="6" fill="#1464a8"/><text x="543" y="1009">Production</text>
      <rect x="597" y="1002" width="6" height="6" fill="#e8401c"/><text x="607" y="1009">Meetings</text>
      <rect x="654" y="1002" width="6" height="6" fill="#3a9ad8"/><text x="664" y="1009">Training</text>
      <rect x="708" y="1002" width="6" height="6" fill="#f7a21b"/><text x="719" y="1009">Lunch</text>
    </g>
  </svg>
</section>

<!-- workmix utilization -->
<section class="abs card" style="left:610px;top:546px;width:182px;height:270px">
  <svg width="182" height="270" viewBox="762 682 227 337">
    <text class="svg-title" x="777" y="711" font-size="13.5" fill="#222">WORKMIX UTILIZATION</text>
    <text x="777" y="731" font-size="13" fill="#444">03.12.2018</text>
    <g stroke="#fff" stroke-width="1.2">
      <path d="M816.2 841.1 A73 73 0 0 1 927.6 831.4 L896.5 862.5 A29 29 0 0 0 852.2 866.4Z" fill="#4a4a4a"/>
      <path d="M927.6 831.4 A73 73 0 0 1 947.9 895.7 L904.6 888 A29 29 0 0 0 896.5 862.5Z" fill="#c8dc1e"/>
      <path d="M947.9 895.7 A73 73 0 0 1 851 951.6 L866.1 910.3 A29 29 0 0 0 904.6 888Z" fill="#16a0b8"/>
      <path d="M851 951.6 A73 73 0 0 1 809.9 913.9 L849.7 895.3 A29 29 0 0 0 866.1 910.3Z" fill="#4a4a4a"/>
      <path d="M809.9 913.9 A73 73 0 0 1 816.2 841.1 L852.2 866.4 A29 29 0 0 0 849.7 895.3Z" fill="#c8dc1e"/>
    </g>
    <g font-size="11" text-anchor="middle">
      <text x="882" y="789" fill="#333">30%</text>
      <text x="941" y="815" fill="#c8dc1e">10%</text>
      <text x="934" y="947" fill="#16a0b8">40%</text>
      <text x="832" y="959" fill="#333">15%</text>
      <text x="794" y="837" fill="#c8dc1e">40%</text>
    </g>
    <g fill="none" stroke-width="1">
      <path d="M870 790 H894 L896 808" stroke="#555"/><path d="M930 816 H952 M930 816 L924 826" stroke="#c8dc1e"/>
      <path d="M921 948 H945 M921 948 L918 936" stroke="#16a0b8"/><path d="M820 960 H845 L850 950" stroke="#555"/>
      <path d="M783 839 H806 L808 850" stroke="#c8dc1e"/>
    </g>
  </svg>
</section>

<!-- tech breakdown -->
<section class="abs card" style="left:801px;top:546px;width:192px;height:270px">
  <svg width="192" height="270" viewBox="1001 682 240 337">
    <text class="svg-title" x="1019" y="711" font-size="13.5" fill="#222">TECH BREKDOWN</text>
    <text x="1019" y="730" font-size="13" fill="#444">03.12.2018</text>
    <g stroke="#c8c8c8" stroke-width="1">
      <line x1="1064" y1="752" x2="1064" y2="976" stroke="#888"/><line x1="1086" y1="752" x2="1086" y2="976"/>
      <line x1="1108" y1="752" x2="1108" y2="976"/><line x1="1130" y1="752" x2="1130" y2="976"/><line x1="1152" y1="752" x2="1152" y2="976"/>
      <line x1="1174" y1="752" x2="1174" y2="976"/><line x1="1196" y1="752" x2="1196" y2="976"/><line x1="1218" y1="752" x2="1218" y2="976"/>
    </g>
    <g fill="#1464a8">
      <rect x="1064" y="800" width="9" height="10"/><rect x="1064" y="838" width="112" height="11"/>
      <rect x="1064" y="882" width="139" height="11"/><rect x="1064" y="930" width="100" height="11"/>
    </g>
    <g font-size="9.5" fill="#444" text-anchor="end">
      <text x="1058" y="760">Loan</text><text x="1058" y="769">out</text>
      <text x="1058" y="803">Loan</text><text x="1058" y="812">in</text>
      <text x="1058" y="839">Activated</text><text x="1058" y="849">techs</text>
      <text x="1058" y="885">Activated</text><text x="1058" y="895">techs</text>
      <text x="1058" y="935">scheduled</text><text x="1058" y="945">techs</text>
    </g>
    <g font-size="10" fill="#444" text-anchor="middle">
      <text x="1061" y="991">0</text><text x="1079" y="991">20</text><text x="1099" y="991">40</text><text x="1120" y="991">60</text>
      <text x="1141" y="991">80</text><text x="1164" y="991">100</text><text x="1191" y="991">120</text><text x="1218" y="991">140</text>
    </g>
  </svg>
</section>

<!-- skills vs jobs -->
<section class="abs card" style="left:1000px;top:546px;width:182px;height:270px">
  <svg width="182" height="270" viewBox="1250 682 227 337">
    <text class="svg-title" x="1272" y="711" font-size="13.5" fill="#222">SKILLS VS JOBS</text>
    <text x="1272" y="734" font-size="13" fill="#444">03.12.2018</text>
    <g font-size="10" fill="#333" text-anchor="middle">
      <text x="1309" y="803">#Jobs</text><text x="1361" y="799">#Skill</text><text x="1361" y="811">Tech</text>
      <text x="1414" y="803">JPT</text><text x="1457" y="803">HPT</text>
    </g>
    <rect x="1250" y="825" width="43" height="41" fill="#f7a21b"/>
    <rect x="1250" y="866" width="43" height="43" fill="#1464a8"/>
    <g fill="none" stroke="#fff" stroke-width="1.5">
      <path d="M1250 825 H1477 M1250 866 H1477 M1250 909 H1477 M1293 825 V909 M1336 825 V909 M1383 825 V909 M1437 825 V909"/>
    </g>
    <g font-size="10" font-weight="700" fill="#fff" text-anchor="middle">
      <text x="1269" y="847">DTV</text><text x="1273" y="889">FIBER</text>
    </g>
    <g font-size="13" fill="#333" text-anchor="middle">
      <text x="1312" y="850">30</text><text x="1359" y="850">10</text><text x="1410" y="850">3</text><text x="1455" y="850" fill="#e2231a" font-weight="700">9.5</text>
      <text x="1312" y="894">55</text><text x="1359" y="894">14</text><text x="1410" y="894" fill="#e2231a" font-weight="700">3.93</text><text x="1455" y="894" fill="#e2231a" font-weight="700">10</text>
    </g>
  </svg>
</section>

<footer class="abs footer">
  <span class="abs" style="left:0;width:1200px;top:18px;text-align:center">Copyrights @ 2018 All Rights Reserved</span>
  <span class="abs" style="left:1154px;top:21px">X37</span>
</footer>

</body>
</html>
```